Business Card Design Project

We have a logo design and are now looking for a business card design. We supply pre-construction services to the Wireless Telecommunication Industry in the development of cell phone tower and other antenna supporting infrastructure e.g. buildings. The types of services include Real Estate Leasing, Zoning & Permitting,Surveying and A&E work. I am looking for a card that includes the logo we have selected along with the full company name. Company colors are Blue and Silver. I want something professional and that "pops". Use your imagination with the four sided star portion of the logo - it can be stretched such that it occupies a large portion of the card or kept simple the way it is. I am interested in seeing the design on a white, silver, navy, black or charcoal background or any other color you think works well with the logo. Apart from the logo that includes HRM we also need to see the full company name on the card - Harborline Relay Maintenance, Inc. The design must also show a persons name, title, address, (2) phone numbers, e-mail address and web address www.hrm.example

Target Market(s)

Cell phone carriers e.g. Quellport Mobile, BN&K, Zandex Cell, Ovalo etc.

Industry/Entity Type

Cell Phone

Requirements
Must have
• Logo and
Harborline Relay Maintenance, Inc.

```html
<!DOCTYPE html>
<html lang="en">
<head>
<meta charset="utf-8">
<title>HRM Business Cards</title>
<link href="https://fonts.googleapis.com/css2?family=Open+Sans:wght@400;700;800&family=Tinos:wght@400;700&display=swap" rel="stylesheet">
<style>
  :root {
    --page: #e4e6e9;
    --charcoal: #2a2829;
    --black: #050505;
    --blue: #1a8fe0;
    --bar-blue: #0d5fb8;
    --white: #ffffff;
    --silver: #c9ccd0;
    --rule: #8a8a8a;
    --sans: "Open Sans", Arial, sans-serif;
    --serif: "Tinos", "Times New Roman", serif;
  }
  * { box-sizing: border-box; margin: 0; padding: 0; }
  html, body { width: 1200px; height: 786px; overflow: hidden; }
  body { background: var(--page); position: relative; font-family: var(--sans); }

  .card { position: absolute; box-shadow: 0 6px 18px rgba(0,0,0,.35); color: var(--white); }

  /* Front card */
  .card-front { left: 80px; top: 150px; width: 560px; height: 300px; background: var(--charcoal); }
  .side-bar { position: absolute; top: 30px; width: 9px; height: 240px; background: var(--bar-blue); border-radius: 5px; }
  .side-bar.left { left: 0; border-radius: 0 5px 5px 0; }
  .side-bar.right { right: 0; border-radius: 5px 0 0 5px; }

  .brand { position: absolute; left: 60px; top: 100px; width: 220px; }
  .wordmark { display: flex; align-items: center; gap: 10px; font-family: var(--sans); font-weight: 800; color: var(--blue); }
  .wordmark .dot { background: var(--blue); border-radius: 50%; flex: none; }
  .brand .wordmark { font-size: 44px; }
  .brand .wordmark .dot { width: 26px; height: 26px; }
  .company-name { margin-top: 14px; font-family: var(--serif); font-weight: 700; font-size: 15px; line-height: 1.25; }

  .divider { position: absolute; left: 290px; top: 30px; width: 1px; height: 200px; background: var(--rule); }

  .contact { position: absolute; left: 306px; top: 24px; }
  .person-name { font-family: var(--serif); font-weight: 700; font-size: 16px; }
  .person-title { font-family: var(--serif); font-weight: 700; font-size: 12px; margin-top: 2px; }
  .contact-list { list-style: none; margin-top: 22px; font-size: 14px; }
  .contact-list li { display: flex; align-items: center; gap: 8px; height: 23px; }
  .contact-list svg { width: 12px; height: 12px; fill: var(--white); flex: none; }
  .address { margin-top: 12px; margin-left: 20px; font-size: 12px; line-height: 1.35; }

  /* Tagline card */
  .card-tagline { left: 650px; top: 90px; width: 520px; height: 300px; background: var(--black); text-align: center; }
  .card-tagline .wordmark { justify-content: center; font-size: 64px; margin-top: 38px; }
  .card-tagline .wordmark .dot { width: 34px; height: 34px; }
  .tagline { margin: 32px auto 0; width: 440px; font-size: 14.5px; letter-spacing: 2.4px; line-height: 1.3; }
  .card-tagline .web { margin-top: 22px; font-family: var(--serif); font-weight: 700; font-size: 16px; letter-spacing: 3px; }

  /* Brand card */
  .card-mark { left: 225px; top: 470px; width: 560px; height: 300px; background: var(--black); text-align: center; }
  .card-mark .wordmark { justify-content: center; font-size: 110px; margin-top: 52px; line-height: 1; }
  .card-mark .wordmark .dot { width: 48px; height: 48px; }
  .card-mark .web { margin-top: 22px; font-size: 18px; letter-spacing: 3px; }
</style>
</head>
<body>

<section class="card card-front">
  <span class="side-bar left"></span>
  <span class="side-bar right"></span>

  <div class="brand">
    <div class="wordmark"><span class="dot"></span>HRM</div>
    <p class="company-name">Harborline Relay Maintenance, Inc.</p>
  </div>

  <span class="divider"></span>

  <div class="contact">
    <p class="person-name">Your Name</p>
    <p class="person-title">Title</p>
    <ul class="contact-list">
      <li><svg viewBox="0 0 24 24"><path d="M6.6 10.8a15.1 15.1 0 0 0 6.6 6.6l2.2-2.2a1 1 0 0 1 1-.25 11.4 11.4 0 0 0 3.6.57 1 1 0 0 1 1 1V20a1 1 0 0 1-1 1A17 17 0 0 1 3 4a1 1 0 0 1 1-1h3.5a1 1 0 0 1 1 1c0 1.25.2 2.45.57 3.57a1 1 0 0 1-.25 1z"/></svg>555-014-6743</li>
      <li><svg viewBox="0 0 24 24"><path d="M6 2h12v6H6zM3 9h18a2 2 0 0 1 2 2v6h-4v5H5v-5H1v-6a2 2 0 0 1 2-2zm4 8v3h10v-3z"/></svg>555-018-4539</li>
      <li><svg viewBox="0 0 24 24"><path d="M2 5h20v14H2zm2 2v.5l8 5 8-5V7z"/></svg>support@hrm.example</li>
      <li><svg viewBox="0 0 24 24"><path d="M12 2a10 10 0 1 0 0 20 10 10 0 0 0 0-20zm-1 2.1V11H4.1A8 8 0 0 1 11 4.1zm2 0A8 8 0 0 1 19.9 11H13zM4.1 13H11v6.9A8 8 0 0 1 4.1 13zm8.9 6.9V13h6.9a8 8 0 0 1-6.9 6.9z"/></svg>www.hrm.example</li>
    </ul>
    <p class="address">4180 Quarry Bend Lane<br>Eastmoor, Texas 70000-0000</p>
  </div>
</section>

<section class="card card-tagline">
  <div class="wordmark"><span class="dot"></span>HRM</div>
  <p class="tagline">HRM keeps you ahead of the competition with fast and accurate execution of all aspects of site acquisition.</p>
  <p class="web">www.hrm.example</p>
</section>

<section class="card card-mark">
  <div class="wordmark"><span class="dot"></span>HRM</div>
  <p class="web">www.hrm.example</p>
</section>

</body>
</html>
```